Cole Varga Photography

Would like the Business card to have a cool logo. I’m targeting wedding/ engagement: portrait photography. My phone number on it. And my business email address.

Wedding/portrait/engagement photography.

```html
<!DOCTYPE html>
<html lang="en">
<head>
<meta charset="utf-8">
<title>Cole Varga Photography – Business Card</title>
<link rel="stylesheet" href="https://fonts.googleapis.com/css2?family=Montserrat:wght@400;600&family=Open+Sans:wght@400;600&display=swap">
<style>
  :root {
    --backdrop: #3a3a38;
    --card-black: #121212;
    --card-white: #f4f4f4;
    --ink-dark: #1c1c1c;
    --ink-mid: #6a6a6a;
    --gloss: #2e2e2e;
    --front-tag: #8a8a8a;
    --lockup-light: #f2f2f2;
  }
  * { margin: 0; padding: 0; box-sizing: border-box; }
  html, body { width: 1200px; height: 824px; overflow: hidden; }
  body {
    position: relative;
    background: var(--backdrop);
    font-family: "Open Sans", Arial, sans-serif;
  }
  .card {
    position: absolute;
    width: 504px;
    height: 288px;
    border-radius: 3px;
    box-shadow: 0 10px 24px rgba(0,0,0,.35);
  }
  .card-front {
    left: 66px; top: 120px;
    background: var(--card-black);
    display: flex; flex-direction: column; align-items: center; justify-content: center;
  }
  .card-back {
    left: 630px; top: 120px;
    background: var(--card-white);
    display: flex; align-items: center;
    padding: 0 40px 0 46px;
  }
  .brand-name {
    font-family: "Montserrat", Arial, sans-serif;
    font-weight: 600;
    letter-spacing: .02em;
    line-height: 1;
    white-space: nowrap;
  }
  .brand-sub {
    font-family: "Montserrat", Arial, sans-serif;
    font-weight: 400;
    letter-spacing: .42em;
    line-height: 1;
    white-space: nowrap;
  }
  .card-front .brand-name { font-size: 40px; color: var(--gloss); }
  .card-front .brand-sub { font-size: 12px; color: var(--gloss); margin-top: 10px; }
  .card-front .services {
    margin-top: 26px;
    font-size: 10.5px;
    letter-spacing: .06em;
    color: var(--front-tag);
    text-transform: uppercase;
  }
  .back-brand { display: flex; flex-direction: column; align-items: center; width: 210px; }
  .card-back .brand-name { font-size: 25px; color: var(--ink-dark); }
  .card-back .brand-sub { font-size: 8px; color: var(--ink-mid); margin-top: 6px; }
  .contact-list { list-style: none; margin-left: 44px; }
  .contact-item {
    display: flex; align-items: center;
    font-size: 14px; font-weight: 600; color: var(--ink-dark);
    line-height: 1; margin: 8px 0;
  }
  .contact-item svg { width: 12px; height: 12px; margin-right: 12px; fill: var(--ink-dark); flex: none; }
  .lockup {
    position: absolute; left: 66px; top: 620px;
    display: flex; flex-direction: column; align-items: center;
  }
  .lockup .brand-name { font-size: 36px; color: var(--lockup-light); }
  .lockup .brand-sub { font-size: 11px; color: var(--lockup-light); margin-top: 12px; padding-left: .42em; }
</style>
</head>
<body>
  <section class="card card-front" aria-label="Card front">
    <p class="brand-name">COLE VARGA</p>
    <p class="brand-sub">PHOTOGRAPHY</p>
    <p class="services">Wedding | Portrait | Engagement Photography</p>
  </section>

  <section class="card card-back" aria-label="Card back">
    <div class="back-brand">
      <p class="brand-name">COLE VARGA</p>
      <p class="brand-sub">PHOTOGRAPHY</p>
    </div>
    <ul class="contact-list">
      <li class="contact-item">
        <svg viewBox="0 0 12 12" aria-hidden="true"><path d="M3 1 L5 1 L5.6 3.6 L4.3 4.5 Q5.2 6.8 7.5 7.7 L8.4 6.4 L11 7 L11 9 Q11 11 9 11 Q1 10 1 3 Q1 1 3 1 Z"/></svg>
        000 000 0000
      </li>
      <li class="contact-item">
        <svg viewBox="0 0 12 12" aria-hidden="true"><path d="M0.5 2.5 H11.5 V9.5 H0.5 Z M1.2 3 L6 6.6 L10.8 3 Z" fill-rule="evenodd"/></svg>
        youremail@xyz.com
      </li>
      <li class="contact-item">
        <svg viewBox="0 0 12 12" aria-hidden="true"><circle cx="6" cy="6" r="5.2" fill="none" stroke="#1c1c1c" stroke-width="1.1"/><ellipse cx="6" cy="6" rx="2.2" ry="5.2" fill="none" stroke="#1c1c1c" stroke-width="1"/><path d="M1 6 H11 M1.8 3.5 H10.2 M1.8 8.5 H10.2" stroke="#1c1c1c" stroke-width=".9"/></svg>
        www.website.com
      </li>
    </ul>
  </section>

  <div class="lockup">
    <p class="brand-name">COLE VARGA</p>
    <p class="brand-sub">PHOTOGRAPHY</p>
  </div>
</body>
</html>
```